Lumen Harbor Business Card Design Project

We have recently rebranded and would like to design new business cards that incorporate the corporate logo - double sided cards with corporate logo on one side and contact details on the other

Target Market(s)

Sophisticated and high net worth investors and finance industry professionals

Industry/Entity Type

Funds Management

Contact Information for Business Card

The card should prominently feature the company name and logo. Other details will be standard contact details for each staff member - name, address, phone, email, website

Colors
0054AA
0677BA
7BADD7
CADEEF
E8F1F8

Requirements
Must have
• Double-sided design with one side prominently featuring the corporate logo and the other side with all standard contact details

```html
<!DOCTYPE html>
<html lang="en">
<head>
<meta charset="utf-8">
<title>Lumen Harbor Business Cards</title>
<link href="https://fonts.googleapis.com/css2?family=Open+Sans:wght@400;600;700&display=swap" rel="stylesheet">
<style>
  :root {
    --backdrop: #acacac;
    --card-dark: #0b111a;
    --card-light: #ffffff;
    --navy: #1f4677;
    --accent: #6a9bcf;
    --ink: #0d0d0d;
    --muted: #737373;
    --wordmark-light: #ffffff;
  }
  * { margin: 0; padding: 0; box-sizing: border-box; }
  html, body {
    width: 1200px; height: 1000px; overflow: hidden;
    background: var(--backdrop);
    font-family: "Open Sans", Arial, sans-serif;
  }
  .canvas { position: relative; width: 1200px; height: 1000px; }
  .card {
    position: absolute; top: 338px;
    width: 514px; height: 296px;
  }
  .card--front { left: 57px; background: var(--card-dark); }
  .card--back { left: 614px; background: var(--card-light); }

  .front-wordmark {
    position: absolute; left: 0; right: 0; top: 124px;
    text-align: center;
    color: var(--wordmark-light);
    font-weight: 600; font-size: 36px; letter-spacing: 1px;
  }

  .back-wordmark {
    position: absolute; right: 33px; top: 62px;
    color: var(--navy);
    font-weight: 600; font-size: 22px; letter-spacing: 0.5px;
  }

  .person { position: absolute; left: 37px; top: 163px; }
  .person__name {
    color: var(--accent); font-weight: 700; font-size: 14px;
    letter-spacing: 1.6px; line-height: 17px; text-transform: uppercase;
  }
  .person__role {
    color: var(--ink); font-weight: 700; font-size: 14px;
    letter-spacing: 1.4px; line-height: 17px; text-transform: uppercase;
  }
  .divider {
    position: absolute; left: 37px; top: 210px;
    width: 445px; height: 2px; background: var(--accent);
  }
  .contact-list, .address {
    position: absolute; top: 224px;
    list-style: none; color: var(--muted);
    font-size: 14px; line-height: 17px;
  }
  .contact-list { left: 37px; }
  .contact-list li { display: flex; align-items: center; }
  .contact-list svg { width: 11px; height: 11px; margin-right: 5px; fill: var(--navy); }
  .address { left: 308px; display: flex; }
  .address svg { width: 10px; height: 14px; margin: 2px 9px 0 0; fill: var(--navy); flex: none; }
</style>
</head>
<body>
<div class="canvas">
  <section class="card card--front">
    <div class="front-wordmark">Lumen Harbor</div>
  </section>

  <section class="card card--back">
    <div class="back-wordmark">Lumen Harbor</div>

    <div class="person">
      <div class="person__name">Daniel Hartley</div>
      <div class="person__role">Portfolio Manager</div>
    </div>

    <div class="divider"></div>

    <ul class="contact-list">
      <li>
        <svg viewBox="0 0 12 12" aria-hidden="true"><path d="M2.5 1l2 2.2-1 1.3c.7 1.5 1.8 2.6 3.2 3.3l1.3-1 2.2 2-1.2 1.8C5.6 10.4 1.6 6.4 1 2.3z"/></svg>
        +02 9000 4417
      </li>
      <li>
        <svg viewBox="0 0 12 12" aria-hidden="true"><path d="M1 2.5h10v7H1zm1 1v.3l4 2.8 4-2.8v-.3zm0 1.5v3.5h8V5L6 7.8z"/></svg>
        invest@lumenharbor.com
      </li>
      <li>
        <svg viewBox="0 0 12 12" aria-hidden="true"><path d="M6 1a5 5 0 100 10A5 5 0 006 1zm0 1c.6.6 1 1.6 1.1 3H4.9C5 3.6 5.4 2.6 6 2zM2.1 5h1.8c.1-1 .3-1.9.7-2.6A4 4 0 002.1 5zm5.3-2.6c.4.7.6 1.6.7 2.6h1.8a4 4 0 00-2.5-2.6zM2.1 6a4 4 0 002.5 3.6c-.4-.7-.6-1.6-.7-2.6zm2.8 0c.1 1.4.5 2.4 1.1 3 .6-.6 1-1.6 1.1-3zm3.2 0c-.1 1-.3 1.9-.7 2.6A4 4 0 009.9 6z"/></svg>
        www.lumenharbor.com
      </li>
    </ul>

    <div class="address">
      <svg viewBox="0 0 10 14" aria-hidden="true"><path d="M5 0a5 5 0 00-5 5c0 3.5 5 9 5 9s5-5.5 5-9a5 5 0 00-5-5zm0 3a2 2 0 110 4 2 2 0 010-4z"/></svg>
      <div>Level 14 Meridian House,<br>52 Carrow Street,<br>Sydney NSW 2000</div>
    </div>
  </section>
</div>
</body>
</html>
```